Digital Album Cover - Where The Quiet River Bends (Piano & Cello)

HiI would like a digital album coverTitle: "Where The Quiet River Bends (Piano & Cello)"Artist: "Lorcan Pettigrew & The Oduya Priscilla"

• Original creativity
• Copyrighted images

```html
<!DOCTYPE html>
<html lang="en">
<head>
<meta charset="UTF-8">
<title>Where The Quiet River Bends (Piano &amp; Cello) – Album Cover</title>
<link rel="stylesheet" href="https://fonts.googleapis.com/css2?family=Tulpen+One&display=swap">
<style>
  :root {
    --bg-core: #352f32;
    --bg-edge: #2a2527;
    --art-light: rgba(206, 198, 201, 0.85);
    --art-mid: rgba(140, 131, 134, 0.6);
    --art-gold: rgba(178, 154, 104, 0.55);
    --text: #ece3e6;
  }
  html, body {
    margin: 0;
    padding: 0;
    width: 1200px;
    height: 1200px;
    overflow: hidden;
    background: var(--bg-edge);
  }
  .album-cover {
    position: relative;
    width: 1200px;
    height: 1200px;
    background: radial-gradient(ellipse 70% 80% at 50% 40%, var(--bg-core) 0%, var(--bg-edge) 100%);
  }
  .cover-art {
    position: absolute;
    left: 190px;
    top: 120px;
    width: 770px;
    height: 790px;
    background:
      linear-gradient(180deg, var(--art-gold) 0%, rgba(178, 154, 104, 0) 30%),
      radial-gradient(ellipse 50% 50% at 50% 55%, var(--art-light) 0%, var(--art-mid) 55%, rgba(53, 47, 50, 0) 100%);
    -webkit-mask-image: radial-gradient(ellipse 52% 52% at 50% 50%, #000 60%, transparent 100%);
    mask-image: radial-gradient(ellipse 52% 52% at 50% 50%, #000 60%, transparent 100%);
  }
  .album-title {
    position: absolute;
    left: 0;
    width: 100%;
    top: 924px;
    margin: 0;
    text-align: center;
    font-family: "Tulpen One", sans-serif;
    font-weight: 400;
    font-size: 58px;
    line-height: 1;
    letter-spacing: 1px;
    text-transform: uppercase;
    color: var(--text);
  }
  .album-artist {
    position: absolute;
    left: 0;
    width: 100%;
    top: 1040px;
    margin: 0;
    text-align: center;
    font-family: "Tulpen One", sans-serif;
    font-weight: 400;
    font-size: 64px;
    line-height: 1;
    letter-spacing: 1px;
    color: var(--text);
  }
</style>
</head>
<body>
  <main class="album-cover">
    <div class="cover-art" role="img" aria-label="Painted heart filled with a misty silver and gold starry nebula texture"></div>
    <h1 class="album-title">Where The Quiet River Bends (Piano &amp; Cello)</h1>
    <p class="album-artist">Lorcan Pettigrew &amp; The Oduya Priscilla</p>
  </main>
</body>
</html>
```